Homepage design for Dutch Job Posting Site (Vakmeld.nl)

We need a redesign of our homepage www.Vakmeld.nl to make it very clear what we do. We are an online job posting portal and are looking to recruit clients and professionals on a single page.

The Homepage will focus on CLIENTS (OPDRACHTGEVERS), with the idea that if we have a lot of jobs posted, then the professionals will come.

Important to know is that we now have ONE REGISTRATION for both professionals and clients - so there is no need for two separate registration options.

Also important to know is that the JOB POSTER pages will have a GREEN hyperlinks color (see the color above the OPDRACHTGEVER at the top of the screen) and the Professionals will have a BLUE hyperlinks color (see the color above the PROFESSIONAL at the top of the screen).

At the top of the page, we would like a 4 page slider (we will do the coding but just want 4 slides) that shows how it works and what makes us unique. In the examples below, you can see that we have already done 2 of them, and we will ask the designer to help do the other two once the project is awarded.

You can see from the images provided that we have already done most of the work. The HEADER WRAP and the FOOTER are already done, and you can use these in your examples.

Notice also in the image "Homepage-BannerBlank" the image used in the center. It is an image that is only as wide as the header and then fades off into a background image that we can use repeat-x in the css of the site which fills the screen on any monitor resolution. If you don't understand what I just wrote, you probably are not the right designer for the job.

Notice also that the two images "NU AANMELDEN" and "VAKMELD ESCROW" use background images that have a SUBTLE background image - it is not just a gradient color change. This is what we LOVE in the design so far.

You can see that our design is already very far advanced, so what we are looking for in a new design are not the overall redesign, but specific, subtle design improvements to give the page a CLEAN, FRESH, MODERN look without being busy and crowded.

Where we specifically want help is in these areas. The designers that show us these elements will be the ones selected. All others will be eliminated without further comment:
a) How to blend in the Vakmeld logo into the header design without taking up more HEIGHT (we have done a white overlay, but this is where you can prove to us that you are great.

b) We need a font for our h1 tags in our site. This will be the same font used in "Laatste Opdrachten" "Laatste Blogs" "Zoek uw professional per categorie of rubriek". Do not use a webfont (Arial or Verdana). Instead, refer to the examples provided for inspiration of a font that best suits the site for a header.

c) We need better containers for "Laatse opdrachten", "Laatste Blogs" and Zoek uw professional per categorie of rubriek. They can have colors or just borders or just outlines. They should compliment the site look though and not distract from it.

d) Transitions between the containers and other elements. Right now they are all just boxy and separate, but there could be some overlap, some shadows, an image divider (as there is between "Laatste Blogs" and TornQX) but again, the transitions need top complement the design and not take it over.

Sites that appeal to us for what we are looking for are:
- plumvo.com
- www.ferlindo.com*
- Marblequist.com*
- Tindelvane.com*
*What we like here are both the top PROMINENT central message and then the smaller subtler design transitions underneath.

Feel free to use images or icons to complement the look, but it must be clean, fresh and modern.

Target Market(s)

University-educated Job Posters between 18 - 45

Industry/Entity Type

Online

Requirements
Must have
• - The header wrapper height but be exactly as it is on the images given. This header will be used on all the inner pages and therefore cannot be any higher than what is shown.
- Focus on the 4 tasks outlined
- Keep it clean! We love white, but also like small icons where appropriate and clean transitions.
Nice to have
• Dutch text is NOT important, we can translate.
Should not have
• No cluttered design.

```html
<!DOCTYPE html>
<html lang="nl">
<head>
<meta charset="utf-8">
<title>Vakmeld – Samen aan de slag</title>
<link href="https://fonts.googleapis.com/css2?family=Open+Sans:ital,wght@0,400;0,600;0,700;1,400;1,600;1,700&family=PT+Sans:ital,wght@0,400;0,700;1,400;1,700&family=Archivo+Narrow:wght@500&family=Arimo:ital,wght@0,400;0,700;1,400;1,700&display=swap" rel="stylesheet">
<style>
:root{
  --green:#7dba1e;
  --green-dark:#4f8a0c;
  --green-light:#a4d43c;
  --ink:#333333;
  --muted:#8a8a8a;
  --line:#dcdcdc;
  --band:#5c5c5c;
  --band-dark:#4d4d4d;
  --card:#3f3f3f;
  --footer:#3b3b3b;
  --bar:#1f1f1f;
  --white:#ffffff;
}
*{box-sizing:border-box;margin:0;padding:0}
html,body{width:900px;height:1200px;overflow:hidden;background:var(--white)}
body{font-family:"Open Sans",Arial,sans-serif;color:var(--ink)}
.page{position:relative;width:900px;height:1200px;overflow:hidden;
  background:linear-gradient(#ffffff 0,#f6f6f6 420px)}
a{color:inherit;text-decoration:none}
.abs{position:absolute}

/* header */
.header-rule{left:0;top:44px;width:900px;height:1px;background:var(--line)}
.brand{left:91px;top:-6px;width:276px;height:110px;background:var(--white);
  box-shadow:0 3px 8px rgba(0,0,0,.28);transform:rotate(-1.2deg);
  display:flex;align-items:center;justify-content:center;gap:12px}
.brand-dot{width:26px;height:26px;border-radius:50%;background:var(--green)}
.brand-name{font-family:"Open Sans",sans-serif;font-weight:700;font-size:40px;color:#3a3a3a;letter-spacing:-1px}
.audience{left:428px;top:22px;font-size:12px;color:#555;display:flex;gap:12px}
.audience .active{color:var(--green-dark);border-top:2px solid var(--green);padding-top:1px;margin-top:-3px}
.account{left:676px;top:22px;font-size:12px;color:#333}
.main-nav{left:388px;top:66px;display:flex;font-size:12px;font-weight:600;color:var(--green-dark)}
.main-nav a{padding:3px 9px;margin-right:12px}
.main-nav .current{background:var(--green);color:var(--white);border-radius:3px}

/* hero */
.hero-title{left:0;width:900px;top:150px;text-align:center;font-family:"Archivo Narrow","Open Sans",sans-serif;
  font-weight:500;font-size:25px;color:#2f2f2f;letter-spacing:.5px}
.hero-map{left:133px;top:207px;width:227px;height:133px;border-radius:40px 60px 30px 50px;
  background:radial-gradient(ellipse at center,#c8c8c8,#e4e4e4 70%,rgba(246,246,246,0))}
.hero-people{left:393px;top:200px;width:174px;height:147px;border-radius:50%;
  background:radial-gradient(circle at 50% 60%,#9a9a9a,#cfcfcf 55%,rgba(246,246,246,0) 72%)}
.hero-badges{left:613px;top:240px;width:108px;height:60px;border-radius:6px;
  background:linear-gradient(#7a7a7a,#4a4a4a)}
.hero-arrow{position:absolute}
.slider-dots{left:109px;top:389px;display:flex;gap:4px}
.slider-dots span{width:12px;height:12px;border-radius:50%;background:#d4d4d4;border:1px solid #bdbdbd}
.slider-dots span:first-child{background:#a9a9a9}
.cta-register{left:303px;top:367px;width:300px;height:44px;border-radius:4px;
  background:linear-gradient(#9fd33a,#6aa916 55%,#5b9810);box-shadow:0 2px 3px rgba(0,0,0,.3);
  display:flex;align-items:center;padding-left:13px;gap:12px;color:var(--white);font-size:21px;font-weight:600}
.cta-register .go{width:24px;height:24px;border-radius:50%;background:#3f6e0a;display:flex;align-items:center;justify-content:center}

/* grey band */
.band{left:0;top:420px;width:900px;height:589px;
  background:repeating-linear-gradient(45deg,rgba(255,255,255,.025) 0 2px,transparent 2px 4px),
  linear-gradient(var(--band-dark),var(--band) 140px,#5e5e5e)}

/* search panel */
.search{left:91px;top:420px;width:718px;height:149px;background:var(--white);
  box-shadow:0 3px 8px rgba(0,0,0,.45)}
.search-divider{left:362px;top:20px;width:1px;height:92px;background:var(--line)}
.search h2{position:absolute;font-family:"PT Sans",sans-serif;font-style:italic;font-weight:400;font-size:20px;color:var(--green-dark)}
.field{position:absolute;height:19px;border:1px solid #bcbcbc;background:var(--white);font-size:9px;
  padding:3px 5px;color:#333;display:flex;justify-content:space-between;align-items:center}
.field .caret{width:12px;height:12px;border:1px solid #999;background:#eee;display:flex;align-items:center;justify-content:center}
.hint{position:absolute;font-size:7.5px;color:#555}
.btn{position:absolute;background:linear-gradient(#95cc33,#5f9d12);color:var(--white);font-weight:700;
  font-size:11px;display:flex;align-items:center;justify-content:center;border-radius:2px;white-space:nowrap}
.search-foot{position:absolute;font-size:10px;font-style:italic;color:#666}
.radio-badge{left:626px;top:111px;width:72px;height:24px;background:#c8161d}

/* cards */
.card{top:587px;width:220px;height:229px;background:var(--card);border:1px solid #2e2e2e;
  box-shadow:0 2px 6px rgba(0,0,0,.45)}
.card h3{position:absolute;left:0;top:8px;width:100%;text-align:center;font-family:"PT Sans",sans-serif;
  font-weight:700;font-size:15px;color:var(--green-light)}
.card-inner{position:absolute;left:18px;top:36px;width:184px;height:77px;background:var(--white);border:2px solid #cfcfcf;display:flex}
.card-art{width:72px;height:100%;background:linear-gradient(#eeeeee,#c9c9c9)}
.card-inner p{padding:7px 6px 0 4px;font-size:10px;font-style:italic;font-weight:700;line-height:13px;color:#333}
.card ul{position:absolute;left:8px;top:131px;list-style:none;font-family:"Arimo",Arial,sans-serif;font-size:9.2px;color:#eee;line-height:16px;white-space:nowrap}
.card li::before{content:"→";margin-right:5px;color:#ddd}
.card .btn{left:65px;top:187px;width:139px;height:26px;font-size:11.5px;border-radius:3px}

/* latest jobs */
.latest{left:583px;top:587px;width:222px}
.latest h3{font-family:"PT Sans",sans-serif;font-weight:700;font-size:15px;color:var(--green-light);
  padding:7px 0 6px;border-bottom:1px solid #777}
.job{height:129px;border-bottom:1px solid #777;padding-top:10px;position:relative;font-family:"Arimo",Arial,sans-serif}
.job h4{font-size:11px;font-style:italic;font-weight:700;color:var(--white)}
.job .tag{font-size:9px;font-style:italic;color:var(--green-light);line-height:13px}
.job p{font-size:8.5px;line-height:11.4px;color:#9c9c9c;margin-top:2px}
.job .meta{position:absolute;left:0;top:108px;width:100%;font-size:9px;color:#eee;display:flex;justify-content:space-between}
.job .meta a{color:var(--green-light);font-style:italic;font-weight:700}

/* welcome */
.welcome{left:98px;top:834px;width:446px;color:var(--white)}
.welcome h2{font-family:"PT Sans",sans-serif;font-weight:700;font-size:18px;margin-bottom:5px}
.welcome h2 span{color:var(--green-light)}
.welcome p{font-size:8.6px;line-height:12.5px;margin-bottom:12px}

/* footer */
.footer{left:0;top:1009px;width:900px;height:151px;background:var(--footer);border-top:1px solid #2a2a2a}
.footer-brand{left:104px;top:16px;display:flex;align-items:center;gap:8px}
.footer-brand .brand-dot{width:20px;height:20px;background:#9a9a9a}
.footer-brand .brand-name{font-size:28px;color:#b5b5b5}
.footer-col{position:absolute;top:18px}
.footer-col h5{font-size:10px;font-weight:700;font-style:italic;color:var(--white);margin-bottom:10px}
.footer-col li{list-style:none;font-size:8.8px;line-height:12.3px;color:#e6e6e6}
.footer-col li.more{color:var(--green-light);font-style:italic;font-weight:600}
.bottom-bar{left:0;top:1160px;width:900px;height:40px;background:var(--bar);color:var(--white);font-size:9px;font-weight:600}
.bottom-bar .copy{position:absolute;left:99px;top:14px}
.bottom-bar .follow{position:absolute;left:683px;top:11px;display:flex;align-items:center;gap:4px}
.follow span.sq{width:10px;height:10px;border-radius:2px;background:#5a7fbf}
</style>
</head>
<body>
<div class="page">

  <div class="abs header-rule"></div>
  <div class="abs brand"><span class="brand-dot"></span><span class="brand-name">Vakmeld</span></div>
  <nav class="abs audience"><a class="active">Opdrachtgever</a><a>Professional</a></nav>
  <div class="abs account">Aanmelden &nbsp;|&nbsp; Inloggen</div>
  <nav class="abs main-nav">
    <a class="current">Home</a><a>Opdrachten</a><a>Mijn Kantoor</a><a>Hoe het werkt</a><a>Blog</a>
  </nav>

  <h1 class="abs hero-title">GET WORLD CLASS WERKT. ONLINE. 100% VEILIG EN RISICO-FREE</h1>
  <div class="abs hero-map" role="img" aria-label="Grijze wereldkaart"></div>
  <svg class="hero-arrow" style="left:360px;top:228px" width="46" height="26" viewBox="0 0 46 26">
    <path d="M2 22 Q20 4 40 10" fill="none" stroke="#8a8a8a" stroke-width="2.5"/>
    <path d="M34 4 L42 10 L34 16" fill="none" stroke="#8a8a8a" stroke-width="2.5"/>
  </svg>
  <div class="abs hero-people" role="img" aria-label="Groep figuren met tekstballonnen"></div>
  <svg class="hero-arrow" style="left:566px;top:228px" width="46" height="26" viewBox="0 0 46 26">
    <path d="M2 22 Q20 4 40 10" fill="none" stroke="#8a8a8a" stroke-width="2.5"/>
    <path d="M34 4 L42 10 L34 16" fill="none" stroke="#8a8a8a" stroke-width="2.5"/>
  </svg>
  <div class="abs hero-badges" role="img" aria-label="Twee hangende kwaliteitsbordjes"></div>
  <div class="abs slider-dots"><span></span><span></span><span></span><span></span></div>
  <a class="abs cta-register">Klik hier voor registratie
    <span class="go"><svg width="10" height="12" viewBox="0 0 10 12"><path d="M2 1 L8 6 L2 11" fill="none" stroke="#fff" stroke-width="2.4"/></svg></span>
  </a>

  <div class="abs band"></div>

  <section class="abs search">
    <div class="abs search-divider"></div>
    <h2 style="left:49px;top:3px">Zoek Professionals</h2>
    <div class="field" style="left:21px;top:36px;width:160px">Vul hier uw zoekopdracht in</div>
    <div class="field" style="left:186px;top:36px;width:160px">Alle categorieën <span class="caret"><svg width="6" height="4"><path d="M0 0 L6 0 L3 4Z" fill="#333"/></svg></span></div>
    <div class="hint" style="left:21px;top:59px">De juiste Professional vinden voor uw opdracht</div>
    <div class="btn" style="left:22px;top:72px;width:76px;height:20px">Zoeken</div>

    <h2 style="left:402px;top:3px">Zoek Opdrachten</h2>
    <div class="field" style="left:374px;top:36px;width:160px">Vul hier uw zoekopdracht in</div>
    <div class="field" style="left:541px;top:36px;width:160px">Alle categorieën <span class="caret"><svg width="6" height="4"><path d="M0 0 L6 0 L3 4Z" fill="#333"/></svg></span></div>
    <div class="hint" style="left:374px;top:59px">Verdien geld door de juiste Opdracht te vinden.</div>
    <div class="btn" style="left:375px;top:72px;width:76px;height:20px">Zoeken</div>

    <div class="search-foot" style="left:18px;top:118px">Wilt u meer Advance Search?</div>
    <div class="btn" style="left:164px;top:115px;width:138px;height:20px;font-size:8.5px">Klik hier voor Advance zoeken</div>
    <div class="search-foot" style="left:356px;top:118px">Zoals gehoord op TornQX! Beluister direct onze radiospot</div>
    <div class="abs radio-badge" role="img" aria-label="Radiozender badge"></div>
  </section>

  <article class="abs card" style="left:97px">
    <h3>Aanmelden als Opdrachtgever</h3>
    <div class="card-inner">
      <div class="card-art" role="img" aria-label="Twee figuren die elkaar de hand schudden"></div>
      <p>Schrijf u nu in bij Vakmeld, plaats geheel gratis uw opdrachten en</p>
    </div>
    <ul>
      <li>Stop de zoektocht naar de juiste professional</li>
      <li>Laat professionals vechten om uw opdracht</li>
      <li>Betaal op een veilige wijze</li>
    </ul>
    <a class="btn">Read More</a>
  </article>

  <article class="abs card" style="left:331px">
    <h3>Aanmelden als Professional</h3>
    <div class="card-inner">
      <div class="card-art" role="img" aria-label="Twee figuren met puzzelstukken"></div>
      <p>Schrijf u nu geheel gratis in bij Vakmeld, kies het juiste abonnement en</p>
    </div>
    <ul>
      <li>Vind eenvoudig nieuwe opdrachten</li>
      <li>Creëer uw online portfolio voor klanten</li>
      <li>Regel al uw zaken via uw Virtuele Kantoor</li>
    </ul>
    <a class="btn">Read More</a>
  </article>

  <aside class="abs latest">
    <h3>Laatste Opdrachten</h3>
    <div class="job">
      <h4>VOIP telefonie in kantoor instellen</h4>
      <div class="tag">IT</div>
      <p>Voor mijn kantoor tot 5 werkplekken ben ik op zoek naar een bedrijf dat de telefonie voor mij op de juiste wijze kan instellen. Ik heb een Belvox online nummer, wat het vaste telefoonnummer moet worden, waarop alle medewerkers te bereiken zijn. Verder moet er doorverbonden kunnen worden naar specifi...</p>
      <div class="meta"><span>7 dagen geleden</span><a>Opdracht bekijken &gt;</a></div>
    </div>
    <div class="job">
      <h4>VOIP telefonie in kantoor instellen</h4>
      <div class="tag">IT</div>
      <p>Voor mijn kantoor tot 5 werkplekken ben ik op zoek naar een bedrijf dat de telefonie voor mij op de juiste wijze kan instellen. Ik heb een Belvox online nummer, wat het vaste telefoonnummer moet worden, waarop alle medewerkers te bereiken zijn. Verder moet er doorverbonden kunnen worden naar specifi...</p>
      <div class="meta"><span>7 dagen geleden</span><a>Opdracht bekijken &gt;</a></div>
    </div>
    <div class="job" style="border-bottom:0">
      <h4>VOIP telefonie in kantoor instellen</h4>
      <div class="tag">IT</div>
      <p>Voor mijn kantoor tot 5 werkplekken ben ik op zoek naar een bedrijf dat de telefonie voor mij op de juiste wijze kan instellen. Ik heb een Belvox online nummer, wat het vaste telefoonnummer moet worden, waarop alle medewerkers te bereiken zijn. Verder moet er doorverbonden kunnen worden naar specifi...</p>
      <div class="meta"><span>7 dagen geleden</span><a>Opdracht bekijken &gt;</a></div>
    </div>
  </aside>

  <section class="abs welcome">
    <h2>Welcome to <span>Vakmeld</span></h2>
    <p>Lorem Ipsum is simply dummy text of the printing and typesetting industry. Lorem Ipsum has been the industry's standard dummy text ever since the 1500s, when an unknown printer took a galley of type and scrambled it to make a type specimen book. It has survived not only five centuries, but also the leap into electronic typesetting, remaining essentially unchanged. It was popularised in the 1960s with the release of Kernaset sheets containing Lorem Ipsum passages, and more recently with desktop publishing software like Orvel PageMaster including versions of Lorem Ipsum.</p>
    <p>Lorem Ipsum is simply dummy text of the printing and typesetting industry. Lorem Ipsum has been the industry's standard dummy text ever since the 1500s, when an unknown printer took a galley of type and scrambled it to make a type specimen book. It has survived not only five centuries, but also the leap into .</p>
  </section>

  <footer class="abs footer">
    <div class="abs footer-brand"><span class="brand-dot"></span><span class="brand-name">Vakmeld</span></div>
    <div class="footer-col" style="left:280px">
      <h5>Zoek opdrachten per categorie</h5>
      <ul>
        <li>Advies &amp; Educatie</li><li>Design &amp; Multimedia</li><li>Dieren</li>
        <li>Engineering / Manufacturing</li><li>Evenementen en Vrije tijd</li>
        <li>Financiëel &amp; Administratief</li><li>Gezondheid, Welzijn en Mens</li>
        <li class="more">Bekijk alles</li>
      </ul>
    </div>
    <div class="footer-col" style="left:452px">
      <h5>Opdrachtgevers</h5>
      <ul><li>Plaats uw opdracht</li><li>Zoek professionals</li><li>Mijn Kantoor</li></ul>
    </div>
    <div class="footer-col" style="left:577px">
      <h5>Professionals</h5>
      <ul><li>Zoek opdrachten</li><li>Mijn Kantoor</li></ul>
    </div>
    <div class="footer-col" style="left:687px">
      <h5>Bedrijf</h5>
      <ul>
        <li>Over Vakmeld</li><li>Hoe het werkt</li><li>FAQ</li><li>Contact</li>
        <li>Privacy beleid</li><li>Financiëel &amp; Administratief</li><li>Geschillenregeling</li>
      </ul>
    </div>
  </footer>
  <div class="abs bottom-bar">
    <span class="copy">© 2011 Vakmeld.nl . All Rights Reserved</span>
    <span class="follow">Volg ons op: &nbsp;<span class="sq"></span><span class="sq"></span><span class="sq"></span><span class="sq" style="background:#e08a2a"></span></span>
  </div>

</div>
</body>
</html>
```